Commercial Real Estate

We need a business card design for a new commercial real estate business that specializes in apartment building brokerage. Not individual units but the entire complex. We find and represent the owners existing buildings and well as new buyers for those buildings. The design should convey trust, integrity, knowledge and growth. It should be easily read.

Target Market(s)

40 to 65 years old

Industry/Entity Type

Real Estate

```html
<!DOCTYPE html>
<html lang="en">
<head>
<meta charset="utf-8">
<title>Harbor Row Property Investments – Business Card</title>
<link rel="stylesheet" href="https://fonts.googleapis.com/css2?family=Roboto+Condensed:ital,wght@0,400;0,700;1,700&display=swap">
<style>
  :root {
    --teal: #6cc8c8;
    --slate: #4f6162;
    --card-top: #eef8f8;
    --card-bottom: #f9fdfd;
    --page: #e6ecec;
  }
  html, body {
    margin: 0;
    width: 1200px;
    height: 900px;
    overflow: hidden;
    background: var(--page);
    font-family: "Roboto Condensed", "Arial Narrow", sans-serif;
  }
  .card {
    position: absolute;
    left: 366px;
    top: 40px;
    width: 468px;
    height: 820px;
    background: linear-gradient(160deg, var(--card-top), var(--card-bottom) 45%, #f2fafa);
    box-shadow: 0 2px 10px rgba(0,0,0,0.12);
    overflow: hidden;
  }
  .timeline {
    position: absolute;
    inset: 0;
  }
  .text { position: absolute; left: 119px; margin: 0; white-space: nowrap; }
  .person-name {
    top: 146px;
    font-size: 36px;
    line-height: 40px;
    font-weight: 700;
    color: var(--teal);
    letter-spacing: 0.5px;
  }
  .person-role {
    top: 190px;
    font-size: 21px;
    line-height: 24px;
    color: var(--slate);
  }
  .company-name {
    top: 304px;
    font-size: 24px;
    line-height: 28px;
    font-weight: 700;
    color: var(--teal);
  }
  .company-address {
    top: 334px;
    font-size: 25px;
    line-height: 31px;
    color: var(--slate);
  }
  .contact-list {
    top: 445px;
    padding: 0;
    list-style: none;
    font-size: 24px;
    line-height: 39.5px;
    color: var(--slate);
  }
  .contact-web { font-weight: 700; font-style: italic; }
  .brand-name {
    position: absolute;
    left: 184px;
    top: 680px;
    margin: 0;
    font-size: 40px;
    line-height: 44px;
    font-weight: 700;
    color: var(--slate);
    letter-spacing: 2px;
    text-transform: uppercase;
  }
</style>
</head>
<body>
  <article class="card">
    <svg class="timeline" width="468" height="820" viewBox="0 0 468 820" aria-hidden="true">
      <g stroke="var(--slate)" stroke-width="2.4" fill="none">
        <line x1="91.5" y1="0" x2="91.5" y2="440"/>
        <line x1="91.5" y1="606" x2="91.5" y2="638"/>
        <line x1="91.5" y1="782" x2="91.5" y2="820"/>
        <circle class="brand-circle" cx="91.5" cy="710" r="72"/>
      </g>
      <g fill="var(--slate)">
        <!-- person -->
        <rect x="78" y="150" width="27" height="34" fill="var(--card-top)"/>
        <circle cx="91.5" cy="160" r="7"/>
        <path d="M79 181 q0 -13 12.5 -13 q12.5 0 12.5 13 z"/>
        <!-- pin -->
        <rect x="80" y="300" width="23" height="36" fill="var(--card-top)"/>
        <path d="M91.5 333 l-9 -15 a10 10 0 1 1 18 0 z"/>
        <circle cx="91.5" cy="312" r="4" fill="#ffffff"/>
        <!-- phone -->
        <path d="M80 460 q11.5 -9 23 0 l-2 4 h-4 l-1 -3 q-4.5 -2 -9 0 l-1 3 h-4 z"/>
        <rect x="83" y="464" width="17" height="9" rx="1.5"/>
        <!-- mobile -->
        <rect x="85" y="494" width="13" height="20" rx="2"/>
        <rect x="87.5" y="497" width="8" height="9" fill="#ffffff"/>
        <!-- envelope -->
        <rect x="80" y="536" width="23" height="15"/>
        <path d="M80 536 l11.5 9 l11.5 -9" stroke="#ffffff" stroke-width="1.6" fill="none"/>
        <!-- globe -->
        <g stroke="var(--slate)" stroke-width="1.5" fill="none">
          <circle cx="91.5" cy="582" r="9"/>
          <ellipse cx="91.5" cy="582" rx="4" ry="9"/>
          <line x1="82.5" y1="582" x2="100.5" y2="582"/>
        </g>
      </g>
    </svg>

    <h1 class="text person-name">DANIEL HART</h1>
    <p class="text person-role">Managing Director</p>

    <p class="text company-name">Harbor Row Property Investments</p>
    <p class="text company-address">Address, Land dummy<br>dummy dummy City</p>

    <ul class="text contact-list">
      <li class="contact-phone">00 0000 0000</li>
      <li class="contact-mobile">0000 000 000</li>
      <li class="contact-email">daniel.hart@harborrow.com</li>
      <li class="contact-web">www.harborrow.com</li>
    </ul>

    <p class="brand-name">Harbor Row</p>
  </article>
</body>
</html>
```